Velvette by Monica Darsh business cards

I am after a business card that will fit the name of my business - velvette.
I want something classy and sexy and nothing tacky.
Ideas that I like are Zebra print backgrounds glitter back grounds
Two ideas I had were
1. Zebra print in black and white, the name Velvette by Monica Darsh and a shilouette of a woman laying on top of the name. Or instead of zebra a glitter background.
2. Idea very similar except for instead of a woman a pair of lips maybe a hot pink glitter or a gold glitter depending on background with the business name between the lips.
Or you can do something completely different.

Industry/Entity Type

Business

```html
<!DOCTYPE html>
<html lang="en">
<head>
<meta charset="utf-8">
<title>Velvette by Monica Darsh – Business Cards</title>
<link rel="stylesheet" href="https://fonts.googleapis.com/css2?family=Arimo:wght@700&display=swap">
<style>
  :root {
    --backdrop: #e9e4dc;
    --gold-light: #fff4b8;
    --gold-mid: #d9ad45;
    --gold-deep: #7d5a1c;
    --pink: #e8268c;
    --ink: #111111;
    --card-shadow: rgba(40, 28, 10, 0.28);
  }
  * { margin: 0; padding: 0; box-sizing: border-box; }
  html, body {
    width: 1200px;
    height: 784px;
    overflow: hidden;
    background: var(--backdrop);
    font-family: "Arimo", Arial, sans-serif;
  }
  .card-sheet {
    width: 1200px;
    height: 784px;
    display: flex;
    align-items: center;
    justify-content: center;
    gap: 40px;
  }
  .business-card {
    position: relative;
    width: 540px;
    height: 309px;
    border-radius: 4px;
    overflow: hidden;
    box-shadow: 0 10px 28px var(--card-shadow);
  }
  .glitter-field {
    position: absolute;
    inset: 0;
    background: radial-gradient(ellipse at 50% 40%, var(--gold-light) 0%, var(--gold-mid) 45%, var(--gold-deep) 100%);
  }
  .card-content {
    position: relative;
    height: 100%;
    display: flex;
    flex-direction: column;
    align-items: center;
    justify-content: center;
    text-align: center;
  }
  .brand-mark {
    display: flex;
    align-items: center;
    gap: 12px;
    color: var(--pink);
    font-weight: 700;
  }
  .brand-mark .mark-dot {
    border-radius: 50%;
    background: var(--pink);
  }
  .card-back .brand-mark { font-size: 40px; }
  .card-back .mark-dot { width: 22px; height: 22px; }
  .card-front .brand-mark { font-size: 84px; }
  .card-front .mark-dot { width: 44px; height: 44px; }
  .by-line {
    margin-top: 8px;
    font-size: 17px;
    color: var(--ink);
  }
  .owner-name {
    margin-top: 4px;
    font-size: 24px;
    color: var(--pink);
  }
  .contact-list {
    margin-top: 24px;
    list-style: none;
    font-size: 19px;
    line-height: 1.3;
    color: var(--ink);
  }
</style>
</head>
<body>
  <main class="card-sheet">
    <section class="business-card card-back">
      <div class="glitter-field" role="img" aria-label="Gold sequin glitter background with sparkles"></div>
      <div class="card-content">
        <div class="brand-mark"><span class="mark-dot"></span><span>Velvette</span></div>
        <p class="by-line">by</p>
        <p class="owner-name">Monica Darsh</p>
        <ul class="contact-list">
          <li>1592 407 318</li>
          <li>www.velvette.com</li>
        </ul>
      </div>
    </section>
    <section class="business-card card-front">
      <div class="glitter-field" role="img" aria-label="Gold sequin glitter background with sparkles"></div>
      <div class="card-content">
        <div class="brand-mark"><span class="mark-dot"></span><span>Velvette</span></div>
      </div>
    </section>
  </main>
</body>
</html>
```